Webdesign für Anbieter von Erotik-Geschichten
Zielgruppe
Wir sind ein Anbieter von Erotik-Geschichten. Die Marke heisst Lunvo Erotica. Das Erlebnis für die Kunden soll hochwertig und persönlich wirken. Daher in keiner Art und Weise schmuddelig. Die Zielgruppe sind Frauen ab ca. 20-40. Die Geschichten werden frei lesbar sein, d.h. es ist kein Online-Shop sondern mehr eine Art Blog mit verschiedenen Geschichten.
Aufgabenstellung
Wichtig ist uns eine schlichtes, minimalistisches Design (vrgl. Tafelwerk) aber trotzdem hochwertig (leicht luxuriös) wirkend.

```html
<!DOCTYPE html>
<html lang="de">
<head>
<meta charset="utf-8">
<title>Lunvo Erotica – Geschichten</title>
<link rel="stylesheet" href="https://fonts.googleapis.com/css2?family=Bitter:wght@400;500;600;700&family=Open+Sans:wght@400;600&display=swap">
<style>
:root{
  --bg:#333333;
  --bg-dark:#2e2e2e;
  --red:#e5322b;
  --text:#ffffff;
  --muted:#e6e6e6;
  --line:#4a4a4a;
}
*{box-sizing:border-box;margin:0;padding:0}
html,body{width:1200px;height:3483px;overflow:hidden}
body{background:var(--bg);color:var(--text);font-family:'Open Sans',sans-serif;position:relative}
.serif{font-family:'Bitter',serif}

.site-header{position:absolute;top:0;left:0;width:1200px;height:116px;background:var(--bg-dark);display:flex;align-items:center}
.brand{position:absolute;left:74px;top:38px;font-family:'Bitter',serif;font-size:32px;font-weight:500;color:var(--text);letter-spacing:.5px}
.main-nav{position:absolute;left:252px;top:53px;display:flex;gap:34px}
.main-nav a,.footer-nav a{font-family:'Bitter',serif;font-size:14px;color:var(--text);text-decoration:none;letter-spacing:.4px}
.main-nav a.active{color:var(--red)}
.header-tools{position:absolute;right:80px;top:42px;display:flex;align-items:center;gap:22px}
.header-tools svg{width:16px;height:16px;fill:var(--red)}
.btn-upgrade{font-family:'Bitter',serif;font-weight:600;font-size:15px;color:var(--red);border:2px solid var(--red);border-radius:18px;padding:4px 22px}
.avatar{width:38px;height:38px;border-radius:50%;border:2px solid var(--red);background:radial-gradient(circle,#c98a62 0%,#7a3a22 70%)}

.hero{position:absolute;top:116px;left:0;width:1200px;height:462px;background:linear-gradient(90deg,#2f2f2f 0%,#3a3836 38%,#7b6a5e 60%,#a8998d 80%,#c9c4bf 100%)}
.hero-copy{position:absolute;left:76px;top:135px}
.hero-kicker{font-family:'Bitter',serif;font-size:18px}
.hero-title{font-family:'Bitter',serif;font-weight:500;font-size:58px;line-height:58px;margin-top:6px}
.btn-outline{display:inline-block;font-family:'Bitter',serif;font-weight:600;color:var(--red);border:3px solid var(--red);border-radius:24px}
.hero .btn-outline{margin-top:14px;width:156px;height:44px;text-align:center;font-size:19px;line-height:38px}

.intro{position:absolute;top:632px;left:82px;width:600px}
.intro h2,.popular h2{font-family:'Bitter',serif;font-weight:400;font-size:21px;margin-bottom:14px}
.intro p{font-size:14px;line-height:24px;color:var(--muted);margin-bottom:16px}
.popular{position:absolute;top:632px;left:770px;width:300px}
.tag-list{display:flex;flex-wrap:wrap;gap:12px 8px;width:270px;margin-left:-6px}
.tag{display:inline-block;font-family:'Bitter',serif;font-size:11px;font-weight:600;color:var(--red);border:1.5px solid var(--red);border-radius:14px;padding:4px 16px;line-height:15px}

.stories-title{position:absolute;top:894px;left:0;width:1200px;text-align:center;font-family:'Bitter',serif;font-weight:400;font-size:40px;letter-spacing:.5px}
.filters{position:absolute;top:967px;left:354px;display:flex;gap:16px}
.filter{width:153px;height:33px;border:2px solid var(--text);border-radius:17px;display:flex;align-items:center;justify-content:center;gap:14px;font-family:'Bitter',serif;font-weight:600;font-size:14px}
.filter svg{width:14px;height:14px;stroke:var(--text);stroke-width:2.5;fill:none}

.story-col{position:absolute;top:1050px;width:340px;display:flex;flex-direction:column;gap:40px}
.col-a{left:74px}.col-b{left:430px}.col-c{left:785px}
.story-card .thumb{width:340px;display:block}
.story-card h3{font-family:'Bitter',serif;font-weight:400;font-size:21px;margin:26px 0 14px 0}
.story-card p{font-size:14px;line-height:24px;color:var(--muted);margin-bottom:10px;width:320px}
.story-card .tag{margin-left:-4px}

.btn-more{position:absolute;top:3164px;left:417px;width:364px;height:43px;border:3px solid var(--text);border-radius:22px;text-align:center;line-height:37px;font-family:'Bitter',serif;font-weight:600;font-size:19px}

.site-footer{position:absolute;top:3280px;left:0;width:1200px;height:203px;border-top:1px solid var(--line)}
.footer-nav{position:absolute;top:28px;left:0;width:1200px;display:flex;justify-content:center;gap:34px}
.footer-brand{position:absolute;top:76px;left:0;width:1200px;text-align:center;font-family:'Bitter',serif;font-size:40px;font-weight:500}
.footer-legal{position:absolute;top:172px;left:0;width:1200px;display:flex;justify-content:center;gap:56px;font-size:11px;color:#bdbdbd}
.footer-legal a{color:#bdbdbd}
</style>
</head>
<body>

<header class="site-header">
  <div class="brand">Lunvo</div>
  <nav class="main-nav">
    <a class="active" href="#">HOME</a>
    <a href="#">KATEGORIEN</a>
    <a href="#">AUTOREN</a>
    <a href="#">ÜBER UNS</a>
  </nav>
  <div class="header-tools">
    <svg viewBox="0 0 16 16" aria-label="Suche"><circle cx="6.5" cy="6.5" r="4.5" fill="none" stroke="#e5322b" stroke-width="2.2"/><path d="M10 10l4.5 4.5" stroke="#e5322b" stroke-width="2.4"/></svg>
    <svg viewBox="0 0 16 16" aria-label="Merkliste"><path d="M3 1h10v14l-5-4-5 4z"/></svg>
    <svg viewBox="0 0 16 16" aria-label="Benachrichtigungen"><path d="M8 1.5c-2.8 0-4.5 2-4.5 4.8v3.5L2 11.5v1h12v-1l-1.5-1.7V6.3C12.5 3.5 10.8 1.5 8 1.5z"/><circle cx="8" cy="14" r="1.6"/></svg>
    <span class="btn-upgrade">Upgrade</span>
    <div class="avatar" role="img" aria-label="Profilbild"></div>
  </div>
</header>

<section class="hero" role="img" aria-label="Foto einer Frau mit Locken, an eine helle Wand gelehnt sitzend">
  <div class="hero-copy">
    <div class="hero-kicker">BDSM</div>
    <h1 class="hero-title">Zufälle und<br>Konsequenzen</h1>
    <span class="btn-outline">Lesen</span>
  </div>
</section>

<section class="intro">
  <h2>Willkommen bei Lunvo</h2>
  <p>Lorem ipsum dolor sit amet, consectetuer adipiscing elit. Aenean commodo ligula eget dolor. Aenean massa. Cum sociis natoque penatibus et magnis dis parturient montes, nascetur ridiculus mus. Donec quam felis.</p>
  <p>Nullam dictum felis eu pede mollis pretium. Integer tincidunt. Cras dapibus. Vivamus elementum semper nisi. Aenean vulpnean leo ligula, porttitor eu, consequat vitae.</p>
</section>

<section class="popular">
  <h2>Beliebte Fetische</h2>
  <div class="tag-list">
    <span class="tag">Erwischt</span><span class="tag">Fesseln</span><span class="tag">Dildo</span>
    <span class="tag">Das erste Mal</span><span class="tag">Anal</span>
    <span class="tag">dicker Schwanz</span><span class="tag">Homeoffice</span>
    <span class="tag">beobachten</span>
  </div>
</section>

<h2 class="stories-title">Neue Geschichten bei Lunvo</h2>
<div class="filters">
  <div class="filter">Sortiert nach <svg viewBox="0 0 14 14"><path d="M2 5l5 5 5-5"/></svg></div>
  <div class="filter">Kategorie <svg viewBox="0 0 14 14"><path d="M2 5l5 5 5-5"/></svg></div>
  <div class="filter">Autor <svg viewBox="0 0 14 14"><path d="M2 5l5 5 5-5"/></svg></div>
</div>

<div class="story-col col-a">
  <article class="story-card">
    <div class="thumb" style="height:233px;background:linear-gradient(135deg,#b36a45,#d99a6e 60%,#8a4a2e)" role="img" aria-label="Foto von Händen auf einem nackten Rücken"></div>
    <h3>Nächte in Samt und Seide</h3>
    <p>Lorem ipsum dolor sit ao ligula eget dolor. Aenean massa.</p>
    <span class="tag">Traumdate</span>
  </article>
  <article class="story-card">
    <div class="thumb" style="height:380px;background:linear-gradient(135deg,#8a2a1c,#c1593a 50%,#e29a6e)" role="img" aria-label="Foto einer Hand auf roter Spitzenwäsche"></div>
    <h3>Die Flitterwochen</h3>
    <p>Lorem ipsum dolor sit amet, consectetuer adipiscing elit.</p>
    <span class="tag">Romantik</span>
  </article>
  <article class="story-card">
    <div class="thumb" style="height:233px;background:linear-gradient(180deg,#b9c4c6,#8d9a8c 45%,#d4c2ad)" role="img" aria-label="Foto eines Paares am Strand"></div>
    <h3>Die Urlaubsbekanntschaft</h3>
    <p>Lorem ipsum dolor sit amet, consectetuer adipiscing elit.</p>
    <span class="tag">Urlaubssex</span>
  </article>
  <article class="story-card">
    <div class="thumb" style="height:233px;background:linear-gradient(180deg,#e3e3e6,#cfc9c5 55%,#b58a68)" role="img" aria-label="Foto eines Spielzeugs auf einem Holztisch"></div>
    <h3>Ménage à trois</h3>
    <p>Lorem ipsum dolor sit commodo ligula eget dolor. Aenean massa.</p>
    <span class="tag">Dreier</span>
  </article>
</div>

<div class="story-col col-b">
  <article class="story-card">
    <div class="thumb" style="height:379px;background:linear-gradient(90deg,#e8e6e3,#cfc7c0 50%,#ebe9e6)" role="img" aria-label="Foto einer Silhouette hinter einem Vorhang"></div>
    <h3>Der Fremde im Zimmer nebenan</h3>
    <p>Ecommodo ligula eget dolor. Aenean massa.</p>
    <span class="tag">Seitensprung</span>
  </article>
  <article class="story-card">
    <div class="thumb" style="height:234px;background:linear-gradient(135deg,#6b4a32,#a9b6c6 45%,#c63a3a 75%,#c0a27a)" role="img" aria-label="Foto einer liegenden Frau mit rotem Spielzeug"></div>
    <h3>Spass allein</h3>
    <p>Lorem ips odo ligula eget dolor. Aenean massa.</p>
    <span class="tag">Selbstbefriedigung</span>
  </article>
  <article class="story-card">
    <div class="thumb" style="height:380px;background:linear-gradient(160deg,#8f7f70,#c9b7a4 50%,#a4957f)" role="img" aria-label="Foto von Beinen am Strand"></div>
    <h3>Quicky am Strand</h3>
    <p>Lorem ipsum dolor sit amet, odo ligula eget dolor. Aenean massa.</p>
    <span class="tag">Erwischt</span>
  </article>
  <article class="story-card">
    <div class="thumb" style="height:380px;background:linear-gradient(135deg,#b8321e,#d8583a 45%,#6a2a1c)" role="img" aria-label="Foto eines Paares in rotem Licht"></div>
    <h3>Der Fremde in meinem Bett</h3>
    <p>Lorem ipsum dolor sit ligula eget dolor. Aenean massa.</p>
    <span class="tag">Erwischt</span>
  </article>
</div>

<div class="story-col col-c">
  <article class="story-card">
    <div class="thumb" style="height:233px;background:radial-gradient(ellipse at center,#b5562c 0%,#d8c88a 35%,#8f8f4f 55%,#151014 70%)" role="img" aria-label="Foto einer aufgeschnittenen Frucht"></div>
    <h3>Foodporn</h3>
    <p>Lorem ipsum dolor sit amet ommodo ligula eget dolor. Aenean massa.</p>
    <span class="tag">Erwischt</span>
  </article>
  <article class="story-card">
    <div class="thumb" style="height:233px;background:linear-gradient(90deg,#3a3a3a,#9a8f88 50%,#4a4a4a)" role="img" aria-label="Schwarzweissfoto eines Männeroberkörpers"></div>
    <h3>Der beste Freund</h3>
    <p>Lorem ipsum dolor sit amet, consectetuer adipiscing massa.</p>
    <span class="tag">Fantasie</span>
  </article>
  <article class="story-card">
    <div class="thumb" style="height:233px;background:linear-gradient(120deg,#c8bcb0,#b62a2a 50%,#d39a7a)" role="img" aria-label="Foto von roter Spitzenwäsche auf Beinen"></div>
    <h3>Die Wette</h3>
    <p>Aenean commodo ligula eget dolor. Aenean massa.</p>
    <span class="tag">Erwischt</span>
  </article>
  <article class="story-card">
    <div class="thumb" style="height:233px;background:linear-gradient(180deg,#8c6a52,#c98c68 50%,#b0302a)" role="img" aria-label="Foto eines Frauenkörpers in rotem Slip"></div>
    <h3>Mit Finanziellen Interessen</h3>
    <p>Lorem ipsum dolor sit amet, consectetuer adipiscing nean massa.</p>
    <span class="tag">Hurensex</span>
  </article>
  <article class="story-card">
    <div class="thumb" style="height:233px;background:linear-gradient(135deg,#a88f6a,#d8d6d2 45%,#2a3048 70%,#7a7a80)" role="img" aria-label="Foto eines Mannes mit Virtual-Reality-Brille"></div>
    <h3>Cybersex</h3>
    <p>Lorem ipsum dolor sit amet, consectetuer ligula eget dolor. Aenean massa.</p>
    <span class="tag">Cybersex</span>
  </article>
</div>

<div class="btn-more">Mehr Geschichten laden</div>

<footer class="site-footer">
  <nav class="footer-nav">
    <a href="#">HOME</a><a href="#">KATEGORIEN</a><a href="#">AUTOREN</a><a href="#">ÜBER UNS</a>
  </nav>
  <div class="footer-brand">Lunvo</div>
  <div class="footer-legal">
    <span>© Lunvo GmbH 2021</span><a href="#">Impressum</a><a href="#">AGB</a><a href="#">Datenschutz</a>
  </div>
</footer>

</body>
</html>
```